Ternisa cleaning service in bellevue

we are cleaning service company. We need a brochure to market our service. Its on demand cleaning service. No appointment necessary. Live like a celebrity type of cleaning service. Once they make a call the cleaning is done within in one hour.

Rates: Swift and Stormy $50, Quest Unbeatable $75 and Vanquisher $100

Industry/Entity Type

Cleaning Service

Font styles to use
Decorative
Script

Colors
9bcb3b
3176b5
85cae6
86cfc6
f68d4d

Requirements
Must have
• One call, you can live like a celebrity. Ternisa cleaning service is licensed and bonded, and will arrive prepared with all supplies needed to leave your home looking amazing.
• If you’re not 100% satisfied, money back guaranteed.
• our Logo
Nice to have
• BATHROOMS
• In your bathrooms, we’re going to:
• Dust light fixtures and remove cobwebs
• Remove smudges from cabinets, drawers, doors, and light switches
• Scrub clean the shower, tile, and tub
• Scrub clean the bathroom fixtures
• Hand-wash all mirrors and shower glass
• Scrub clean the toilet
• Remove all trash and reline trash can
• Hand wash all baseboards and floors
• KITCHENS
• Wipe down all counters
• Load breakfast dishes into the dishwasher
• Clean the sink
• Clean the microwave inside and out
• Clean the exterior of the refrigerator, over, and stove top
• Wipe down tables and chairs
• Dust or vacuum baseboards
• Wash floor
• BEDROOMS
• Dust ceiling fans and blinds
• Remove cobwebs
• Wipe down window sills and sashes
• Wipe down and dust picture frames
• Wipe down and dust mirrors
• Tidy up the room
• Make beds with provided sheets
• COMMON LIVING AREAS
• Remove cobwebs
• Smudges removed from doors and light switches
• Dust picture frames and decorations
• Wipe down and dust furniture
• Wipe down exterior of washer and dryer
• Sweep off front porch
• Clean glass on front doors, french doors, and sliding glass doors
• Tidy up where applicable
• Remove all trash and reline trash cans
• Vacuum all carpet and steps
• Vacuum or wash all floors

```html
<!DOCTYPE html>
<html lang="en">
<head>
<meta charset="utf-8">
<title>Ternisa Cleaning Service Brochure</title>
<link rel="stylesheet" href="https://fonts.googleapis.com/css2?family=Oswald:wght@500;700&family=Fjalla+One&family=PT+Sans:ital,wght@0,400;0,700;1,700&family=Poppins:wght@300&display=swap">
<style>
:root{
  --stage:#a97e5a;
  --ink:#111;
  --panel-dark:#161616;
  --green:#9bcb3b;
  --green-deep:#3e7d1e;
  --blue:#3176b5;
  --sky:#85cae6;
  --orange:#f68d4d;
  --red:#ea4a2e;
  --yellow:#e8e23a;
  --white:#fff;
  --paper:#f1f2f2;
}
*{margin:0;padding:0;box-sizing:border-box}
html,body{width:1200px;height:892px;overflow:hidden}
body{background:var(--stage);position:relative;font-family:"PT Sans",sans-serif}
.side-label{position:absolute;top:52px;font-family:"PT Sans",serif;font-size:27px;color:var(--white)}
.side-label.back{left:96px}
.side-label.front{left:968px}
.brochure{position:absolute;left:82px;top:97px;width:1048px;height:720px;background:var(--paper);overflow:hidden;box-shadow:2px 3px 6px rgba(0,0,0,.45)}
.back-panel{position:absolute;left:0;top:0;width:525px;height:720px;background:radial-gradient(ellipse at 60% 30%,#333 0%,var(--panel-dark) 70%)}
.photo{position:absolute;border-radius:7px}
.abs{position:absolute}
.shapes{position:absolute;left:0;top:0}
.rates{position:absolute;left:31px;top:162px;font-family:"Fjalla One",sans-serif;font-size:20px;line-height:29px;color:var(--green)}
.rates li{list-style:none;display:flex}
.rates .name{width:176px}
.no-appointment{position:absolute;left:280px;top:148px;width:230px;height:100px;border-radius:50%;background:radial-gradient(ellipse,#3a3a3a 0%,rgba(40,40,40,.6) 60%,transparent 75%);text-align:center}
.no-appointment h2{font-family:"Fjalla One",sans-serif;font-weight:400;font-size:21px;line-height:26px;color:var(--orange);margin-top:14px}
.no-appointment p{font-size:11px;font-weight:700;color:var(--orange);line-height:14px;margin-top:7px}
.heading{font-family:"Fjalla One",sans-serif;font-size:18px;color:var(--red);font-weight:400}
.list{list-style:none;font-size:8.6px;line-height:14.7px;color:var(--ink)}
.list li{position:relative;padding-left:13px}
.list li::before{content:"";position:absolute;left:0;top:4px;width:7px;height:7px;border-radius:50%;background:#444}
.dark .list{color:var(--white)}
.dark .list li::before{background:var(--orange)}
.intro{font-size:9.5px;font-weight:700;font-style:italic;margin:6px 0 3px}
.contact-bar{position:absolute;left:28px;top:678px;width:457px;height:31px;border-radius:7px;background:var(--green);font-size:14px;color:#222;padding:5px 10px;line-height:20px}
.contact-bar strong{font-size:20px;font-weight:700}
.wordmark{position:absolute;font-family:"PT Sans",sans-serif;font-weight:700;line-height:1;white-space:nowrap}
.wordmark.back{left:360px;top:635px;font-size:34px;color:var(--green)}
.wordmark.front{right:32px;top:40px;font-size:68px;color:var(--blue)}
.pitch{position:absolute;right:26px;text-align:right}
.pitch h2{font-family:"Oswald",sans-serif;font-weight:500;color:var(--white);font-size:36px;line-height:40px}
.pitch h3{font-family:"Oswald",sans-serif;font-weight:500;color:var(--yellow);font-size:25px;line-height:34px}
.pitch p{font-size:13px;font-weight:700;font-style:italic;color:var(--white);line-height:18px;margin-top:8px;width:262px;margin-left:auto}
.call{position:absolute;left:546px;top:536px;color:var(--blue);font-size:16px}
.call strong{font-size:21px}
.satisfaction{position:absolute;left:798px;top:534px;font-family:"Poppins",sans-serif;font-weight:300;font-size:20px;color:var(--blue);letter-spacing:.5px}
.guarantee{position:absolute;left:525px;width:523px;top:688px;text-align:center;font-family:"Oswald",sans-serif;font-weight:500;font-size:15.5px;color:var(--red);letter-spacing:.3px}
</style>
</head>
<body>
<span class="side-label back">(Back)</span>
<span class="side-label front">(Front)</span>

<main class="brochure">
  <section class="back-panel dark"></section>

  <div class="photo abs" role="img" aria-label="Gloved hand scrubbing white tiles with a brush" style="left:525px;top:0;width:523px;height:263px;border-radius:0;background:linear-gradient(160deg,#fafafa 0%,#e9ebea 50%,#d7e6b4 70%,#a6cf58 85%,#eef0ef 100%)"></div>

  <svg class="shapes" width="1048" height="720" viewBox="0 0 1048 720" aria-hidden="true">
    <polygon points="0,263 883,263 608,516 0,493" fill="var(--green)"/>
    <polygon points="608,516 883,263 883,292 680,493" fill="var(--green-deep)"/>
    <polygon points="822,291 1048,291 1048,518 608,518" fill="var(--red)"/>
    <line x1="226" y1="270" x2="226" y2="486" stroke="#d8efa8" stroke-width="1.5"/>
    <circle cx="155" cy="400" r="62" fill="none" stroke="#c5e389" stroke-width="1"/>
    <circle cx="155" cy="400" r="50" fill="#b2d965" opacity=".5"/>
    <circle cx="335" cy="330" r="44" fill="none" stroke="#c5e389" stroke-width="1"/>
    <circle cx="800" cy="590" r="45" fill="#cfe6a8" opacity=".4"/>
    <circle cx="850" cy="560" r="28" fill="#cfe6a8" opacity=".4"/>
    <ellipse cx="774" cy="547" rx="10" ry="8" fill="var(--green)"/>
  </svg>

  <div class="photo" role="img" aria-label="Gloved hands cleaning a steel sink" style="left:30px;top:36px;width:124px;height:110px;background:linear-gradient(135deg,#4aa0c0,#b9bcbd)"></div>
  <div class="photo" role="img" aria-label="Blue-gloved hand wiping an oven door" style="left:161px;top:36px;width:177px;height:110px;background:linear-gradient(135deg,#7a6a4c,#c9b98e 50%,#3c7ec0)"></div>
  <div class="photo" role="img" aria-label="Vacuuming a wooden floor in a living room" style="left:346px;top:36px;width:152px;height:110px;background:linear-gradient(180deg,#e7a07c,#7a3a22)"></div>

  <ul class="rates">
    <li><span class="name">Swift and Stormy</span><span>$50</span></li>
    <li><span class="name">Quest Unbeatable</span><span>$75</span></li>
    <li><span class="name">Vanquisher</span><span>$100</span></li>
  </ul>

  <div class="no-appointment">
    <h2>No Appointment<br>Necessary</h2>
    <p>Once they make a call the cleaning<br>is done within in one hour.</p>
  </div>

  <section class="abs" style="left:25px;top:276px;width:200px">
    <h2 class="heading">BATHROOMS</h2>
    <p class="intro">In your bathrooms, we’re going to:</p>
    <ul class="list">
      <li>Dust light fixtures and remove cobwebs</li>
      <li>Remove smudges from cabinets, drawers, doors, and light switches</li>
      <li>Scrub clean the shower, tile, and tub</li>
      <li>Scrub clean the bathroom fixtures</li>
      <li>Hand-wash all mirrors and shower glass</li>
      <li>Scrub clean the toilet</li>
      <li>Remove all trash and reline trash can</li>
      <li>Hand wash all baseboards and floors</li>
    </ul>
  </section>

  <section class="abs" style="left:238px;top:276px;width:290px">
    <h2 class="heading" style="margin-bottom:5px">KITCHENS</h2>
    <ul class="list">
      <li>Dust light fixtures and remove cobwebs</li>
      <li>Remove smudges from cabinets, drawers, doors, and light switches</li>
      <li>Wipe down all counters</li>
      <li>Load breakfast dishes into the dishwasher</li>
      <li>Clean the sink</li>
      <li>Clean the microwave inside and out</li>
      <li>Clean the exterior of the refrigerator, over, and stove top</li>
      <li>Wipe down tables and chairs</li>
      <li>Remove all trash and reline trash can</li>
      <li>Dust or vacuum baseboards</li>
      <li>Wash floor</li>
    </ul>
  </section>

  <section class="abs" style="left:550px;top:276px;width:200px">
    <h2 class="heading" style="margin-bottom:5px">BEDROOMS</h2>
    <ul class="list">
      <li>Dust ceiling fans and blinds</li>
      <li>Remove cobwebs</li>
      <li>Wipe down window sills and sashes</li>
      <li>Wipe down and dust picture frames</li>
      <li>Wipe down and dust mirrors</li>
      <li>Tidy up the room</li>
      <li>Make beds with provided sheets</li>
      <li>Remove all trash and reline trash can</li>
      <li>Dust or vacuum baseboards</li>
    </ul>
  </section>

  <section class="abs dark" style="left:28px;top:500px;width:400px">
    <h2 class="heading" style="margin-bottom:6px">COMMON LIVING AREAS</h2>
    <div style="display:flex;gap:18px">
      <ul class="list" style="width:162px">
        <li>Dust ceiling fans and blinds</li>
        <li>Remove cobwebs</li>
        <li>Wipe down window sills and sashes</li>
        <li>Smudges removed from doors and light switches</li>
        <li>Wipe down and dust mirrors</li>
        <li>Dust picture frames and decorations</li>
        <li>Wipe down and dust furniture</li>
      </ul>
      <ul class="list" style="width:170px">
        <li>Sweep off front porch</li>
        <li>Clean glass on front doors, french doors, and sliding glass doors</li>
        <li>Tidy up where applicable</li>
        <li>Remove all trash and reline trash cans</li>
        <li>Dust or vacuum baseboards</li>
        <li>Vacuum all carpet and steps</li>
        <li>Vacuum or wash all floors</li>
      </ul>
    </div>
  </section>

  <div class="contact-bar">For more details call: <strong>000.000.0000</strong></div>
  <div class="wordmark back">Ternisa</div>

  <div class="wordmark front">Ternisa</div>

  <div class="pitch" style="top:303px">
    <h2>One Call</h2>
    <h3>you can live like<br>a celebrity</h3>
    <p>Ternisa cleaning service is licensed and bonded, and will arrive prepared with all supplies needed to leave your home looking amazing.</p>
  </div>

  <div class="call">Call Us: <strong>000.000.0000</strong></div>
  <div class="satisfaction">100% SATISFACTION</div>

  <div class="photo" role="img" aria-label="Person vacuuming a carpet beside a white sofa" style="left:546px;top:574px;width:156px;height:101px;background:linear-gradient(180deg,#f3f3f1,#c9c3b8)"></div>
  <div class="photo" role="img" aria-label="Cleaner wiping a white bathtub with green gloves" style="left:707px;top:574px;width:140px;height:101px;background:linear-gradient(135deg,#d9413a,#f1efe9 55%,#8cc43f)"></div>
  <div class="photo" role="img" aria-label="Housekeeper holding folded white towels in a bedroom" style="left:852px;top:574px;width:164px;height:101px;background:linear-gradient(135deg,#e6e0d6,#f7f5f1 50%,#3a3a3a)"></div>

  <p class="guarantee">IF YOU’RE NOT 100% SATISFIED, MONEY BACK GUARANTEED</p>
</main>
</body>
</html>
```